A5, portrait
Theme is science
audience is VIPS, politicians, executives
this is a really important event, we want a very classy invitation
include logo for brook and bloom and nexa but nexa one bigger
images attached
Have attached some styles we like but doesn't need to be these colours. If we can incorporate some colours from our logo would be good but don't make too colourful and childish

You’re invited to the official opening and launch of Nexa, Centre of Wonderment. an industry first, pioneering, STEM hub.

Saturday 30th April, 2022

10:00 am – 12:00 pm

42 Pellow Street, Hadley Vale

Light canapes provided. Dress code is smart/casual

All guests will be given a guided walk through of Australia’s first dedicated STEM education hub for children aged 3-6.

Invitation only

RSVP: 18 April to marketing@brookandbloom.edu.au

```html
<!DOCTYPE html>
<html lang="en">
<head>
<meta charset="utf-8">
<title>Nexa Opening Invitation</title>
<link rel="stylesheet" href="https://fonts.googleapis.com/css2?family=Sacramento&family=Roboto+Slab:wght@300;400;700&family=Roboto:wght@700&family=Rozha+One&display=swap">
<style>
  :root {
    --page-bg: #5a5a5a;
    --paper: #ffffff;
    --night: #0c0d16;
    --night-soft: #1b1d2c;
    --gold: #ffe600;
    --coral: #e2372f;
    --amber: #f3a52a;
    --ink-light: #ffffff;
  }
  * { margin: 0; padding: 0; box-sizing: border-box; }
  html, body {
    width: 960px; height: 1200px; overflow: hidden;
    background: var(--page-bg);
  }
  .invitation {
    position: absolute; left: 57px; top: 0;
    width: 846px; height: 1200px;
    background: var(--paper);
    overflow: hidden;
    font-family: "Roboto Slab", Georgia, serif;
    color: var(--ink-light);
    text-align: center;
  }
  .backdrop {
    position: absolute; left: 18px; top: 18px; right: 18px; bottom: 18px;
    background:
      radial-gradient(ellipse at 50% 62%, rgba(60,64,90,.5), transparent 40%),
      radial-gradient(ellipse at 20% 35%, rgba(70,50,60,.4), transparent 50%),
      radial-gradient(ellipse at 80% 30%, rgba(50,60,80,.4), transparent 50%),
      linear-gradient(180deg, var(--night-soft), var(--night));
  }
  .frame {
    position: absolute; left: 46px; top: 46px; width: 754px; height: 1108px;
    border: 1.6px solid var(--gold);
  }
  .headline-small {
    position: absolute; left: 318px; top: 180px;
    font-family: "Sacramento", cursive; font-size: 50px; line-height: 60px; color: var(--gold);
  }
  .headline-large {
    position: absolute; left: 0; right: 0; top: 168px;
    padding-left: 36px;
    font-family: "Sacramento", cursive; font-size: 190px; line-height: 1;
    color: var(--gold); font-weight: 400;
  }
  .intro {
    position: absolute; left: 0; right: 0; top: 343px;
    font-weight: 300; font-size: 24px; line-height: 32px;
  }
  .event-box {
    position: absolute; left: 140px; top: 484px; width: 566px; height: 144px;
    border: 1.5px solid var(--amber); border-top: none; border-radius: 0 0 8px 8px;
  }
  .box-top {
    position: absolute; top: 484px; width: 50px; height: 10px;
    border-top: 1.5px solid var(--amber);
  }
  .box-top.left { left: 140px; border-left: 1.5px solid var(--amber); border-top-left-radius: 8px; }
  .box-top.right { left: 656px; border-right: 1.5px solid var(--amber); border-top-right-radius: 8px; }
  .event-date {
    position: absolute; left: 0; right: 0; top: 462px;
    font-family: "Rozha One", Georgia, serif; font-size: 34px; line-height: 42px;
    color: var(--coral);
  }
  .event-time {
    position: absolute; left: 142px; top: 516px; width: 562px; height: 48px;
    background: linear-gradient(90deg, transparent 8%, rgba(181,154,18,.9) 25%, rgba(140,120,14,.55) 60%, transparent 92%);
    font-family: "Roboto", Arial, sans-serif; font-weight: 700; font-size: 32px; line-height: 48px;
  }
  .event-address {
    position: absolute; left: 0; right: 0; top: 574px;
    font-family: "Rozha One", Georgia, serif; font-size: 34px; line-height: 42px;
    color: var(--amber);
  }
  .details {
    position: absolute; left: 0; right: 0; top: 652px;
    font-weight: 400; font-size: 29px; line-height: 40px;
  }
  .walkthrough {
    position: absolute; left: 0; right: 0; top: 748px;
    font-size: 20px; line-height: 27px; font-weight: 400;
  }
  .invite-rule {
    position: absolute; top: 850px; width: 119px; height: 1.5px; background: var(--gold);
  }
  .invite-rule.left { left: 114px; }
  .invite-rule.right { left: 613px; }
  .invite-only {
    position: absolute; left: 256px; top: 829px; width: 334px; height: 42px;
    border: 1.5px solid var(--gold); border-radius: 21px;
    font-family: "Rozha One", Georgia, serif; font-size: 31px; line-height: 42px;
    color: var(--gold);
  }
  .rsvp {
    position: absolute; left: 0; right: 0; top: 884px;
    font-size: 20px; line-height: 28px;
  }
  .rsvp strong { font-weight: 700; }
  .brand {
    position: absolute; display: flex; flex-direction: column; align-items: center; gap: 10px;
  }
  .brand-mark { border-radius: 50%; background: var(--gold); }
  .brand-name {
    font-family: "Roboto Slab", Georgia, serif; font-weight: 700;
    color: var(--ink-light); white-space: nowrap;
  }
  .brand-nexa { left: 88px; top: 902px; width: 206px; }
  .brand-nexa .brand-mark { width: 84px; height: 84px; }
  .brand-nexa .brand-name { font-size: 54px; line-height: 60px; }
  .brand-brook { left: 370px; top: 962px; width: 120px; gap: 8px; }
  .brand-brook .brand-mark { width: 48px; height: 48px; }
  .brand-brook .brand-name { font-size: 17px; line-height: 22px; }
</style>
</head>
<body>
  <main class="invitation">
    <div class="backdrop" role="img" aria-label="Dimly lit, softly blurred science lab interior with a glass globe on a display plinth, crossed by fine yellow decorative lines"></div>
    <div class="frame"></div>

    <header>
      <span class="headline-small">You’re</span>
      <h1 class="headline-large">Invited</h1>
    </header>

    <p class="intro">to the official opening and launch of Nexa,<br>Centre of Wonderment. an industry first, pioneering,<br>STEM hub.</p>

    <div class="event-box"></div>
    <span class="box-top left"></span>
    <span class="box-top right"></span>
    <p class="event-date">Saturday 30th April, 2022</p>
    <p class="event-time">10:00 am – 12:00 pm</p>
    <p class="event-address">42 Pellow Street, Hadley Vale</p>

    <p class="details">Light canapes provided.<br>Dress code is smart/casual</p>
    <p class="walkthrough">All guests will be given a guided walk through of Australia’s first<br>dedicated STEM education hub for children aged 3-6.</p>

    <span class="invite-rule left"></span>
    <p class="invite-only">Invitation only</p>
    <span class="invite-rule right"></span>

    <p class="rsvp"><strong>RSVP: 18 April to</strong><br>marketing@brookandbloom.edu.au</p>

    <div class="brand brand-nexa">
      <span class="brand-mark"></span>
      <span class="brand-name">Nexa</span>
    </div>
    <div class="brand brand-brook">
      <span class="brand-mark"></span>
      <span class="brand-name">Brook and Bloom</span>
    </div>
  </main>
</body>
</html>
```